Desserts Business Card Design

I own a dessert business and cakes and cupcakes are my biggest sellers. I have been running this as a part time business since 2007. I am now looking to expand going full time and open a store front within he next 12 months.
With this expansion I am looking to have my own design setup for the business.

I have been using a design on my cards provided to me by a website I got the cards from. I would like a more original design I can use for the cards, the store front and any other advertising I will be doing. I also have a saying on the back of my business card which I would like to be worked in as well.
"Desserts are nothing, if not from scratch"

Target Market(s)

Younger and older families of all ethnic backgrounds

Industry/Entity Type

Advertising

Contact Information for Business Card

Maribel's Sugared Treats
Tobias Fenwick
4417 Pinecrest Terrace
Oshawa, Ontario
M3P 7J2

Logo Text

Logo styles of interest
Emblem Logo
Pictorial/Combination Logo
Wordmark Logo
Lettermark Logo
Requirements
Must have
• "Desserts are nothing, if not from scratch"
Nice to have
• Maribel's Sugared Treats - This can actually be turned into a logo which is really what I am looking for. Using MST, converted to a logo? I am really looking to see what you can provide me with.
A cake or cupcake added on the front of the card?
Should not have
• I cannot think of anything right now. I an looking forward to see the imaginations from the design groups

```html
<!DOCTYPE html>
<html lang="en">
<head>
<meta charset="utf-8">
<title>Maribel's Sugared Treats – Business Card</title>
<link rel="stylesheet" href="https://fonts.googleapis.com/css2?family=Crimson+Text:ital,wght@0,400;0,700;1,400&family=Pacifico&display=swap">
<style>
  :root {
    --backdrop: #eeeeee;
    --berry: #e0267a;
    --berry-deep: #c8156a;
    --butter: #f7b218;
    --butter-light: #fbc53c;
    --cream: #ffffff;
    --ink: #3a2410;
    --card-shadow: rgba(0, 0, 0, 0.18);
  }
  * { box-sizing: border-box; margin: 0; padding: 0; }
  html, body { width: 1200px; height: 813px; overflow: hidden; }
  body { background: var(--backdrop); position: relative; font-family: "Crimson Text", serif; }

  .card {
    position: absolute; left: 270px; width: 660px; height: 377px;
    background: var(--berry); border-radius: 6px; overflow: hidden;
    box-shadow: 0 6px 18px var(--card-shadow);
  }
  .card--front { top: 20px; }
  .card--back { top: 416px; }

  /* front */
  .front-band {
    position: absolute; left: 150px; right: 0; top: 150px; height: 160px;
    background: var(--butter); border-radius: 80px 0 0 80px;
  }
  .treat-art {
    position: absolute; width: 190px; height: 190px; border-radius: 50%;
    background: radial-gradient(circle at 50% 45%, var(--butter-light), var(--butter));
    border: 6px solid var(--cream);
  }
  .card--front .treat-art { left: 42px; top: 108px; }
  .brand-name {
    position: absolute; right: 36px; top: 28px;
    font-family: "Pacifico", cursive; font-size: 40px; color: var(--cream); line-height: 1.2;
  }
  .owner { position: absolute; left: 300px; top: 170px; }
  .owner-name { font-weight: 700; font-size: 32px; color: var(--cream); line-height: 1; }
  .owner-address { font-size: 18px; color: var(--ink); line-height: 1.2; margin-top: 8px; }
  .phone {
    position: absolute; left: 36px; bottom: 18px;
    display: flex; align-items: center; gap: 8px;
    font-weight: 700; font-size: 26px; color: var(--butter);
  }
  .phone svg { width: 22px; height: 22px; }

  /* back */
  .quote {
    position: absolute; left: 40px; top: 24px; color: var(--cream);
    font-style: italic; font-size: 34px; line-height: 1.1;
  }
  .quote-tail { display: block; padding-left: 180px; }
  .back-panel {
    position: absolute; left: 24px; right: 24px; top: 126px; bottom: 24px;
    background: var(--butter); border-radius: 18px;
  }
  .card--back .treat-art { left: 50px; top: 140px; width: 180px; height: 180px; }
  .web {
    position: absolute; right: 48px; top: 220px;
    background: var(--cream); color: var(--berry-deep); border-radius: 20px;
    padding: 6px 22px; font-size: 18px; font-weight: 700;
  }
</style>
</head>
<body>
  <section class="card card--front">
    <div class="front-band"></div>
    <div class="treat-art" role="img" aria-label="Illustration of a cupcake with pink frosting and a cherry on top"></div>
    <div class="brand-name">Maribel's Sugared Treats</div>
    <div class="owner">
      <p class="owner-name">Tobias Fenwick</p>
      <p class="owner-address">4417 Pinecrest Terrace<br>Oshawa, Ontario M3P 7J2</p>
    </div>
    <p class="phone">
      <svg viewBox="0 0 24 24" aria-hidden="true"><path fill="currentColor" d="M6.6 10.8a15 15 0 0 0 6.6 6.6l2.2-2.2a1 1 0 0 1 1-.25 11.4 11.4 0 0 0 3.6.57 1 1 0 0 1 1 1V20a1 1 0 0 1-1 1A17 17 0 0 1 3 4a1 1 0 0 1 1-1h3.5a1 1 0 0 1 1 1c0 1.25.2 2.45.57 3.6a1 1 0 0 1-.25 1z"/></svg>
      289-555-0148
    </p>
  </section>

  <section class="card card--back">
    <p class="quote">“Desserts are nothing,<span class="quote-tail">if not from scratch”</span></p>
    <div class="back-panel"></div>
    <div class="treat-art" role="img" aria-label="Illustration of a cupcake with pink frosting and a cherry on top"></div>
    <p class="web">www.maribelstreats.com</p>
  </section>
</body>
</html>
```